Aviation security consulting company needs a website

We need a website design for Brisk Holloway, and aviation security consulting company. Brisk Holloway (www.briskholloway.example) is an aviation security consulting company that works with government and industry stakeholders in over 60 countries on aviation security strategy, governance, and oversight at the regulatory and operational level.
Brisk Holloway is strongly internationally focused.
The website required should be simple, corporate, serious, and communicate professionalism, reliability and honesty. We are trying to give the company a feeling of being well established.
The attached files include the company logo, along with examples of company web page styles that we like.
The Brisk Holloway website need only be around five pages long (landing page, who we are, our services, our clients, contact), though don't feel limited to only five pages.
The existing website (www.briskholloway.example) was rushed and put together using Wix. We don't love the existing website as it looks too amateur, so don't use it as a template.
There is no requirement for any online sales tools to be included in the site. The site is purely informational, with the option of people making contact via email.

```html
<!DOCTYPE html>
<html lang="en">
<head>
<meta charset="utf-8">
<title>Brisk Holloway – Aviation Security Consulting</title>
<link rel="stylesheet" href="https://fonts.googleapis.com/css2?family=Open+Sans:wght@400;600;700;800&display=swap">
<style>
:root{
  --navy:#1c2b4f;
  --navy-deep:#142140;
  --orange:#f39019;
  --ink:#2a2f3a;
  --muted:#7c8593;
  --band:#eef2f5;
  --line:#d7dde4;
  --white:#ffffff;
}
*{box-sizing:border-box;margin:0;padding:0}
html,body{width:1200px;height:2504px;overflow:hidden}
body{font-family:"Open Sans",Arial,sans-serif;color:var(--ink);background:var(--white);position:relative}

.site-header{height:88px;display:flex;align-items:center;justify-content:space-between;padding:0 140px 0 140px;background:var(--white)}
.brand{display:flex;align-items:center;gap:10px}
.brand-mark{width:40px;height:40px;background:var(--navy)}
.brand-name{font-size:22px;font-weight:700;color:var(--navy);line-height:1}
.brand-tag{font-size:9px;color:var(--muted);letter-spacing:.5px;margin-top:3px}
.main-nav{display:flex;gap:30px;font-size:11px;font-weight:600;color:var(--muted);text-transform:uppercase}
.main-nav .active{color:var(--navy);border-bottom:2px solid var(--orange);padding-bottom:6px}

.hero{height:552px;position:relative;color:var(--white);text-align:center}
.hero-photo{position:absolute;inset:0;background:linear-gradient(180deg,#7fa9cf 0%,#a9c4dc 30%,#8b8f92 62%,#2a2f36 100%)}
.hero-text{position:absolute;left:0;right:0;top:410px}
.hero-title{font-size:52px;font-weight:700;letter-spacing:1px}
.hero-sub{font-size:14px;margin:10px auto 0;width:560px;line-height:1.5}

.section{text-align:center}
.section-title{font-size:28px;font-weight:800;color:var(--navy);text-transform:uppercase}
.divider{display:block;margin:10px auto 0}
.section-lead{font-size:12px;color:var(--muted);width:620px;margin:18px auto 0;line-height:1.6}

.about{height:312px;padding-top:64px}
.about p{font-size:12px;color:var(--muted);width:720px;margin:28px auto 0;line-height:1.7}
.btn-outline{display:inline-block;margin-top:28px;border:2px solid var(--navy);border-radius:20px;padding:6px 22px;font-size:11px;font-weight:700;color:var(--navy)}

.services{height:408px;background:var(--band);padding-top:62px}
.service-list{display:flex;justify-content:center;gap:80px;margin-top:40px}
.service{width:250px}
.service svg{display:block;margin:0 auto}
.service h3{font-size:16px;font-weight:700;color:var(--navy);margin-top:12px}
.service p{font-size:11px;color:var(--muted);line-height:1.6;margin-top:8px}

.clients{height:352px;padding-top:56px}
.client-row{display:flex;justify-content:center;gap:20px;margin-top:40px}
.client{width:150px;height:64px;border:1px solid var(--line);display:flex;align-items:center;justify-content:center;gap:8px;font-size:15px;font-weight:700;color:var(--navy)}
.client i{width:14px;height:14px;border-radius:50%;background:var(--orange);display:block}
.dots{display:flex;justify-content:center;gap:8px;margin-top:40px}
.dots span{width:8px;height:8px;border-radius:50%;background:var(--navy);opacity:.35}
.dots span:first-child{opacity:1}

.contact{height:508px;background:linear-gradient(135deg,#22355f 0%,var(--navy) 55%,var(--navy-deep) 100%);color:var(--white);padding-top:64px}
.contact .section-title{color:var(--white)}
.contact-lead{font-size:12px;margin-top:24px}
.contact-lead b{color:var(--orange)}
.form{width:500px;margin:26px auto 0;display:grid;grid-template-columns:1fr 1fr;gap:14px 16px;text-align:left}
.field{height:36px;background:var(--white);border-radius:3px;font-size:11px;color:var(--muted);padding:10px 12px}
.field.message{grid-column:1 / 3;height:92px}
.btn-solid{display:inline-block;margin-top:26px;background:var(--orange);border-radius:20px;padding:9px 30px;font-size:11px;font-weight:700;color:var(--white)}

.site-footer{height:240px;display:flex;padding:44px 140px 0;gap:0}
.footer-about{width:360px}
.footer-about p{font-size:11px;color:var(--muted);line-height:1.6;margin-top:14px;width:290px}
.footer-col{width:230px}
.footer-col h4{font-size:12px;font-weight:700;color:var(--navy);text-transform:uppercase;margin-bottom:12px}
.footer-col li{list-style:none;font-size:11px;color:var(--muted);margin-bottom:8px;display:flex;align-items:center;gap:8px}
.footer-col li i{width:14px;height:14px;border-radius:50%;background:var(--navy);display:block;flex:none}
.copyright{height:44px;background:var(--band);font-size:10px;color:var(--muted);text-align:center;line-height:44px}
</style>
</head>
<body>

<header class="site-header">
  <div class="brand">
    <span class="brand-mark"></span>
    <div>
      <div class="brand-name">Brisk Holloway</div>
      <div class="brand-tag">aviation security consulting</div>
    </div>
  </div>
  <nav class="main-nav">
    <span class="active">Home</span><span>Who we are</span><span>Our services</span><span>Our clients</span><span>Contact</span>
  </nav>
</header>

<section class="hero">
  <div class="hero-photo" role="img" aria-label="Passenger jet parked at an airport stand with ground service vehicles under a blue sky"></div>
  <div class="hero-text">
    <h1 class="hero-title">BRISK HOLLOWAY</h1>
    <p class="hero-sub">Brisk Holloway works with government and industry on aviation security regulatory and operational strategy, governance, and oversight.</p>
  </div>
</section>

<section class="section about">
  <h2 class="section-title">Who we are ?</h2>
  <svg class="divider" width="160" height="10" viewBox="0 0 160 10"><line x1="0" y1="5" x2="160" y2="5" stroke="#1c2b4f" stroke-width="2"/><rect x="75" y="0" width="10" height="10" transform="rotate(45 80 5)" fill="#f39019"/></svg>
  <p>Brisk Holloway advises civil aviation authorities, airports and airlines on building security programmes that work in practice. Our team brings decades of regulatory and operational experience across more than sixty countries, helping clients design oversight frameworks, train inspectors and meet international standards. We combine careful assessment with practical guidance so every recommendation can be put into action with confidence.</p>
  <span class="btn-outline">READ MORE →</span>
</section>

<section class="section services">
  <h2 class="section-title">Our services</h2>
  <svg class="divider" width="160" height="10" viewBox="0 0 160 10"><line x1="0" y1="5" x2="160" y2="5" stroke="#1c2b4f" stroke-width="2"/><rect x="75" y="0" width="10" height="10" transform="rotate(45 80 5)" fill="#f39019"/></svg>
  <p class="section-lead">We support regulators and industry with clear strategy, sound governance and dependable oversight at every level of aviation security.</p>
  <div class="service-list">
    <div class="service">
      <svg width="48" height="48" viewBox="0 0 48 48" fill="#1c2b4f"><circle cx="24" cy="12" r="7"/><path d="M12 34c0-8 5-13 12-13s12 5 12 13z"/><circle cx="9" cy="20" r="4"/><circle cx="39" cy="20" r="4"/><path d="M2 36c0-5 3-9 7-9s7 4 7 9zM32 36c0-5 3-9 7-9s7 4 7 9z"/></svg>
      <h3>Euismod Turpis Volutpat</h3>
      <p>Independent reviews of national security programmes, with clear findings and practical steps to close every gap.</p>
    </div>
    <div class="service">
      <svg width="48" height="48" viewBox="0 0 48 48" fill="#1c2b4f"><rect x="6" y="28" width="7" height="14"/><rect x="17" y="20" width="7" height="22"/><rect x="28" y="24" width="7" height="18"/><rect x="39" y="12" width="7" height="30"/><polyline points="6,22 20,12 31,17 44,4" fill="none" stroke="#f39019" stroke-width="2"/></svg>
      <h3>Viverra Maximus</h3>
      <p>Risk-based oversight models that help authorities focus inspection resources where they matter most today.</p>
    </div>
    <div class="service">
      <svg width="48" height="48" viewBox="0 0 48 48"><path d="M24 3l17 6v12c0 12-8 20-17 24C15 41 7 33 7 21V9z" fill="none" stroke="#1c2b4f" stroke-width="3"/><polyline points="16,24 22,30 33,18" fill="none" stroke="#f39019" stroke-width="3"/></svg>
      <h3>Dignissim Tincidunt</h3>
      <p>Tailored training for inspectors and managers, built on international standards and real operational cases.</p>
    </div>
  </div>
</section>

<section class="section clients">
  <h2 class="section-title">Our clients</h2>
  <svg class="divider" width="160" height="10" viewBox="0 0 160 10"><line x1="0" y1="5" x2="160" y2="5" stroke="#1c2b4f" stroke-width="2"/><rect x="75" y="0" width="10" height="10" transform="rotate(45 80 5)" fill="#f39019"/></svg>
  <p class="section-lead">Governments, airports and airlines across the world trust our team to strengthen their aviation security programmes.</p>
  <div class="client-row">
    <div class="client"><i></i>Orvale</div>
    <div class="client"><i></i>Emberly</div>
    <div class="client"><i></i>Dunmar</div>
    <div class="client"><i></i>Aluvia</div>
    <div class="client"><i></i>Sunrise Freight</div>
    <div class="client"><i></i>Rivanto</div>
  </div>
  <div class="dots"><span></span><span></span><span></span><span></span><span></span></div>
</section>

<section class="section contact">
  <h2 class="section-title">Contact us</h2>
  <svg class="divider" width="160" height="10" viewBox="0 0 160 10"><line x1="0" y1="5" x2="160" y2="5" stroke="#ffffff" stroke-width="2"/><rect x="75" y="0" width="10" height="10" transform="rotate(45 80 5)" fill="#f39019"/></svg>
  <p class="contact-lead">Let us know in the form below, email at <b>info@briskholloway.example</b> or call us <b>+00 555 0142 88</b></p>
  <div class="form">
    <div class="field">Your Name</div>
    <div class="field">Company Name</div>
    <div class="field">Your Email</div>
    <div class="field">Subject</div>
    <div class="field">Phone</div>
    <div class="field">Where are you from?</div>
    <div class="field message">Message</div>
  </div>
  <span class="btn-solid">SUBMIT NOW</span>
</section>

<footer class="site-footer">
  <div class="footer-about">
    <div class="brand">
      <span class="brand-mark"></span>
      <div>
        <div class="brand-name">Brisk Holloway</div>
        <div class="brand-tag">aviation security consulting</div>
      </div>
    </div>
    <p>Brisk Holloway is an independent aviation security consultancy serving government and industry clients in over sixty countries.</p>
  </div>
  <div class="footer-col">
    <h4>Sitemap</h4>
    <ul><li>› Home</li><li>› Who we are</li><li>› Our services</li><li>› Our clients</li><li>› Contact</li></ul>
  </div>
  <div class="footer-col">
    <h4>Contact us</h4>
    <ul><li><i></i>14 Harbour Lane, Northfield</li><li><i></i>+00 555 0142 88</li><li><i></i>info@briskholloway.example</li></ul>
  </div>
  <div class="footer-col">
    <h4>Follow us</h4>
    <ul><li><i></i>Chirpline</li><li><i></i>Boardnest</li><li><i></i>Friendloop</li><li><i></i>Groupspace</li></ul>
  </div>
</footer>
<div class="copyright">Copyright © 2024 Brisk Holloway. All rights reserved.</div>

</body>
</html>
```